Visit Qalimora Card (School That only teach arabic language) (Guaranteed Payment)

Hi, we are a new school That Teach arabic language in Tunisia, we are looking to conceptulize visit cards for our team. The business card will be printed in color and on Both Sides. We want to communiquer: innovation, excellence, professionalism, leadership and trust. Would we need the business card at the end with the details of everyone of our team (3) General and aussi has one for our center in Tunis. La même designed is used througout of course. Waiting for your sugestions! The address is the Sámi for all the visit cards: 47 Rue des Oliviers Zembra Cedar Building, 3rd Floor 1053 Les Berges du Lac 1, Tunisia aussi la même is the website for all www.qalimora.example The 4 visits Card Those names are: Karim Ouertani Jonas Freiberg Rania Gharbi Qalimora For Karim's Ouertani Visit Card Function name: Managing Partner Phone number: 216 94120386 Email: karim.ouertani@qalimora. example For Rania's visit card function name: Marketing Assistant Phone number: 216 97402615 Email: rania.gharbi@qalimora.example For Jonas's visit card: Function name: Managing Partner Phone number: 49 151 08246519 Mail: @ jonas.freiberg qalimora.example You can find our logo in the attachment.

```html
<!DOCTYPE html>
<html lang="fr">
<head>
<meta charset="utf-8">
<title>Qalimora – cartes de visite</title>
<link rel="stylesheet" href="https://fonts.googleapis.com/css2?family=Arimo:wght@400;700&display=swap">
<style>
  :root {
    --backdrop: #3b3330;
    --card: #151617;
    --card-edge: #1f2022;
    --ink-light: #f1f1f1;
    --ink-silver: #a4a6a8;
    --ink-muted: #8d8f92;
    --brand-blue: #1f6fb5;
    --divider: #c9cbcd;
  }
  * { box-sizing: border-box; margin: 0; padding: 0; }
  html, body { width: 1200px; height: 864px; overflow: hidden; }
  body {
    background: var(--backdrop);
    font-family: "Arimo", Arial, sans-serif;
    position: relative;
  }
  .card {
    position: absolute;
    width: 540px;
    height: 310px;
    background: var(--card);
    border: 1px solid var(--card-edge);
    border-radius: 3px;
    box-shadow: 0 14px 30px rgba(0,0,0,.45);
  }
  .card--front { left: 40px; top: 190px; }
  .card--back  { left: 620px; top: 364px; }

  /* front */
  .front-wordmark {
    position: absolute;
    left: 0; right: 0; top: 96px;
    text-align: center;
    font-size: 64px;
    font-weight: 400;
    color: var(--ink-silver);
    letter-spacing: 1px;
  }
  .front-site {
    position: absolute;
    left: 0; right: 0; top: 206px;
    text-align: center;
    font-size: 13px;
    letter-spacing: 6px;
    color: var(--ink-muted);
  }

  /* back */
  .back-wordmark {
    position: absolute;
    left: 34px; top: 126px;
    font-size: 40px;
    color: var(--brand-blue);
  }
  .back-divider {
    position: absolute;
    left: 268px; top: 60px;
    width: 1px; height: 190px;
    background: linear-gradient(to bottom, transparent, var(--divider) 30%, var(--divider) 70%, transparent);
  }
  .contact {
    position: absolute;
    left: 290px; top: 72px;
    color: var(--ink-light);
    font-size: 13px;
    line-height: 1.35;
  }
  .contact__name { color: var(--brand-blue); font-size: 16px; }
  .contact__role { font-size: 15px; margin-bottom: 10px; }
  .contact__address { margin-bottom: 8px; }
  .contact__line { display: flex; align-items: center; gap: 8px; }
  .contact__icon { width: 12px; height: 12px; flex: none; }
</style>
</head>
<body>

<section class="card card--front" aria-label="Recto">
  <div class="front-wordmark">qalimora</div>
  <div class="front-site">www.qalimora.example</div>
</section>

<section class="card card--back" aria-label="Verso">
  <div class="back-wordmark">qalimora</div>
  <div class="back-divider"></div>
  <div class="contact">
    <div class="contact__name">Karim Ouertani</div>
    <div class="contact__role">Managing Partner</div>
    <div class="contact__address">
      47 Rue des Oliviers Zembra<br>
      Immeuble Cèdres, 3ème étage<br>
      2078 Les Jardins du Golfe 2, Tunisie
    </div>
    <div class="contact__line">
      <svg class="contact__icon" viewBox="0 0 12 12" aria-hidden="true"><path fill="#1f6fb5" d="M2.5 1h2l1 3-1.3.8a6.5 6.5 0 0 0 3 3L8 6.5l3 1v2A1.5 1.5 0 0 1 9.5 11 8.5 8.5 0 0 1 1 2.5 1.5 1.5 0 0 1 2.5 1z"/></svg>
      <span>+216 94 120 386</span>
    </div>
    <div class="contact__line">
      <svg class="contact__icon" viewBox="0 0 12 12" aria-hidden="true"><rect x="0.5" y="2" width="11" height="8" rx="1" fill="#1f6fb5"/><path d="M1 2.5l5 4 5-4" stroke="#151617" fill="none"/></svg>
      <span>karim.ouertani@qalimora.example</span>
    </div>
    <div class="contact__line">
      <svg class="contact__icon" viewBox="0 0 12 12" aria-hidden="true"><circle cx="6" cy="6" r="5.5" fill="#1f6fb5"/><path d="M.5 6h11M6 .5c-2 2-2 9 0 11M6 .5c2 2 2 9 0 11" stroke="#151617" fill="none" stroke-width=".8"/></svg>
      <span>www.qalimora.example</span>
    </div>
  </div>
</section>

</body>
</html>
```